Solar Company Bussiness Card

I need a 2 sided business card and would like a .psd and any font files for each side of the card. I would like my logo used, it should be attached with the fonts. I'm not opposed to the font colors with the logo being changed.

On the sample design, I'd like the following:

Warren Kettle
President
Phone: 570-318-4957
www.brightvalepower.example

As I've recently opened in a 2nd market, I'm not sure about an address as I currently have 2 of them. I may actually get separate cards printed, one batch for each address, that's why I need the PSD file.
Updates

I'm very pleased with the response and designs I've received here for my business card. First and foremost, I'd like to thank everyone who took the time to submit a design. There truly are a lot of great designs in the bunch here and I'm having a little difficulty deciding. I will be reaching out to someone in the next day or two here to go to a final design. At this time, I'm not looking for any new concepts. If any of you do logos, I'm looking for a new logo for our sister entity, Kettle Partners, Inc. Thanks, Warren Kettle

Reason: I'm not looking for any new designs at this point, but extending this deadline in order to give people I've asked a chance to re-submit items.

```html
<!DOCTYPE html>
<html lang="en">
<head>
<meta charset="utf-8">
<title>Brightvale Power — Business Card</title>
<link href="https://fonts.googleapis.com/css2?family=Open+Sans:wght@400;600&display=swap" rel="stylesheet">
<style>
  :root {
    --backdrop: #e6e7e9;
    --card: #ffffff;
    --card-edge: #f2f3f5;
    --brand-blue: #1b5fa3;
    --deep-blue: #0d4f8f;
    --sky-blue: #3aa3e0;
    --ink: #1e1e22;
  }
  * { margin: 0; padding: 0; box-sizing: border-box; }
  html, body {
    width: 1200px; height: 871px; overflow: hidden;
    background: var(--backdrop);
    font-family: "Open Sans", Arial, sans-serif;
  }
  .stage { position: relative; width: 1200px; height: 871px; }
  .card {
    position: absolute; left: 280px; width: 640px; height: 366px;
    background: linear-gradient(135deg, var(--card) 55%, var(--card-edge));
    box-shadow: 0 6px 18px rgba(0,0,0,0.18);
    overflow: hidden;
  }
  .card-front { top: 50px; }
  .card-back { top: 456px; }

  .brand {
    position: absolute; display: flex; align-items: center;
    color: var(--brand-blue); font-weight: 600; white-space: nowrap;
  }
  .brand-mark { background: var(--brand-blue); flex: none; }
  .card-front .brand { left: 0; right: 0; top: 150px; justify-content: center; font-size: 46px; gap: 16px; }
  .card-front .brand-mark { width: 40px; height: 40px; }
  .card-back .brand { left: 40px; top: 92px; font-size: 27px; gap: 10px; }
  .card-back .brand-mark { width: 24px; height: 24px; }

  .contact { position: absolute; left: 360px; top: 90px; color: var(--ink); }
  .contact-name { font-size: 21px; font-weight: 600; letter-spacing: 0.5px; }
  .contact-role { font-size: 15px; color: var(--brand-blue); margin-top: -2px; }
  .contact-lines { list-style: none; margin-top: 22px; }
  .contact-lines li { display: flex; align-items: center; gap: 14px; font-size: 15px; letter-spacing: 0.8px; margin-bottom: 10px; }
  .contact-lines svg { width: 18px; height: 18px; flex: none; }

  .wave { position: absolute; left: 0; bottom: 0; width: 640px; height: 170px; }
</style>
</head>
<body>
<main class="stage">
  <section class="card card-front" aria-label="Card front">
    <div class="brand"><span class="brand-mark"></span>Brightvale Power</div>
  </section>

  <section class="card card-back" aria-label="Card back">
    <div class="brand"><span class="brand-mark"></span>Brightvale Power</div>

    <div class="contact">
      <p class="contact-name">Warren Kettle</p>
      <p class="contact-role">President</p>
      <ul class="contact-lines">
        <li>
          <svg viewBox="0 0 20 20" aria-hidden="true"><path d="M3 7c0-2 3-3 7-3s7 1 7 3v1h-4V6.5H7V8H3z M5 10h10l1 6H4z" fill="var(--deep-blue)"/><circle cx="10" cy="13" r="1.6" fill="#fff"/></svg>
          570-318-4957
        </li>
        <li>
          <svg viewBox="0 0 20 20" aria-hidden="true"><circle cx="10" cy="10" r="8" fill="none" stroke="var(--deep-blue)" stroke-width="2"/><path d="M2 10h16M10 2c-4 5-4 11 0 16M10 2c4 5 4 11 0 16" fill="none" stroke="var(--deep-blue)" stroke-width="1.4"/></svg>
          www.brightvalepower.example
        </li>
      </ul>
    </div>

    <svg class="wave" viewBox="0 0 640 170" preserveAspectRatio="none" aria-hidden="true">
      <path d="M0 10 C120 0 220 40 330 85 C440 130 540 150 640 140 L640 170 L0 170 Z" fill="var(--sky-blue)"/>
      <path d="M0 24 C120 16 220 54 330 98 C440 142 540 160 640 150 L640 170 L0 170 Z" fill="var(--deep-blue)"/>
    </svg>
  </section>
</main>
</body>
</html>
```